Simple Easy - Taekwondo brochure

I have the content and an idea of the layout I want. I need it to look nice and sharp.

It's a sided 8.5x11 colored brochure

please feel free to move things around and use the images provided

my website is www.brightpathdojo.example if you need an understanding of what the business is about.

all text content is on the website. please be creative!

Target Market(s)

Mothers...must by family friendly because it's for mothers to bring their kids.

Industry/Entity Type

Martial Art

Font styles to use
Other font styles liked:
• Lato

```html
<!DOCTYPE html>
<html lang="en">
<head>
<meta charset="utf-8">
<title>Bright Path Dojo Brochure</title>
<link rel="stylesheet" href="https://fonts.googleapis.com/css2?family=Lato:ital,wght@0,400;0,700;0,900;1,400&display=swap">
<style>
:root{
  --ink:#0b0b0b;
  --panel:#141414;
  --card:#1c1c1c;
  --card-edge:#3a3a3a;
  --red:#e3151b;
  --red-dark:#b10d12;
  --white:#ffffff;
  --grey:#cfcfcf;
  --stage:#ececec;
}
*{box-sizing:border-box;margin:0;padding:0}
html,body{width:1200px;height:764px;overflow:hidden;background:var(--stage)}
body{font-family:"Lato",Arial,sans-serif;color:var(--white)}
.brochure{display:flex;width:1200px;height:764px;background:var(--ink)}
.panel{width:400px;height:764px;position:relative;overflow:hidden}

/* Instructor panel */
.instructor{background:linear-gradient(160deg,#1a1a1a 0%,var(--ink) 60%);padding:28px 30px}
.instructor-photo{position:absolute;top:0;right:0;width:190px;height:170px;background:linear-gradient(135deg,#2a2a2a,#9a9a9a 55%,#1a1a1a)}
.instructor-title{margin-top:166px;font-weight:900;font-size:26px;letter-spacing:1px;text-transform:uppercase;text-align:right}
.instructor-title .accent,.testimonial-name .accent{color:var(--red)}
.bio{margin-top:18px;font-size:11.5px;line-height:1.55;color:var(--grey);text-align:justify}
.bio p+p{margin-top:10px}
.awards{margin-top:26px;text-align:center}
.awards-title{color:var(--red);font-weight:900;font-size:13px;letter-spacing:1px}
.awards-sub{font-size:11px;color:var(--grey);margin-bottom:10px}
.awards li{list-style:none;font-size:11.5px;line-height:1.5;margin-bottom:6px}

/* Info panel */
.info{background:var(--panel);padding:22px 18px}
.info-card{height:100%;border:2px solid var(--card-edge);border-radius:18px;background:var(--card);padding:22px 20px;display:flex;flex-direction:column;align-items:center}
.section-title{font-weight:900;font-size:20px;letter-spacing:1px}
.testimonial-name{margin-top:8px;font-weight:900;font-size:14px}
.testimonial{margin-top:10px;font-size:12.5px;line-height:1.6;color:var(--grey);text-align:justify}
.offer{margin-top:28px;position:relative;width:270px;background:linear-gradient(180deg,var(--red),var(--red-dark));border-radius:12px;padding:22px 10px 12px;text-align:center}
.offer-tag{position:absolute;top:-11px;left:50%;transform:translateX(-50%);background:var(--ink);color:var(--red);border:2px solid var(--red);border-radius:12px;font-weight:900;font-size:12px;padding:2px 16px;white-space:nowrap}
.offer-amount{font-weight:900;font-size:42px;line-height:1}
.offer-detail{font-size:12px;font-weight:700;margin-top:4px}
.call{margin-top:22px;display:flex;align-items:center;gap:10px}
.call-label{font-size:18px}
.call-number{font-size:20px;font-weight:900;color:var(--red)}
.contact{margin-top:12px;font-size:11.5px;line-height:1.6;color:var(--grey);text-align:center}
.contact svg{vertical-align:-2px;margin-right:4px}
.map{margin-top:auto;width:100%;height:170px;border-radius:14px;background:linear-gradient(135deg,#e8e6e1,#d9d6cf 50%,#f0ead8)}

/* Cover panel */
.cover{background:linear-gradient(180deg,var(--ink),#161616)}
.brand{position:absolute;top:40px;left:0;right:0;display:flex;align-items:center;justify-content:center;gap:10px}
.brand-dot{width:22px;height:22px;border-radius:50%;background:var(--red)}
.brand-name{font-weight:900;font-size:20px;letter-spacing:1px;text-transform:uppercase}
.kids-photo{position:absolute;top:150px;left:0;width:400px;height:300px;background:linear-gradient(160deg,#2b2b2b,#d8d4cc 45%,#c63a1c 70%,#1c1c1c)}
.cover-rule{position:absolute;top:458px;left:0;width:400px;height:5px;background:var(--red)}
.headline{position:absolute;top:488px;left:34px;text-transform:uppercase;line-height:1}
.headline-top{font-weight:700;font-size:40px;letter-spacing:2px}
.headline-bottom{font-weight:900;font-size:31px;color:var(--red);margin-top:6px}
.web-bar{position:absolute;top:590px;left:0;width:260px;height:26px;background:var(--white);color:var(--ink);font-weight:700;font-size:13px;display:flex;align-items:center;padding-left:28px}
.mascot{position:absolute;top:632px;left:130px;width:150px;height:120px;border-radius:8px;background:linear-gradient(135deg,#c98a3a,#f4f1ea 50%,#6f8f2e)}
</style>
</head>
<body>
<main class="brochure">

  <section class="panel instructor">
    <div class="instructor-photo" role="img" aria-label="Portrait photo of the head instructor in a black-collared uniform"></div>
    <h2 class="instructor-title">Master <span class="accent">Daniel</span></h2>
    <div class="bio">
      <p>Master Daniel is the owner and head instructor of Bright Path Dojo. He began training as a young boy and has taught children and adults for over twenty years. His classes blend discipline, respect and fun so every student grows in confidence.</p>
      <p>He competed on national teams, coached a champion university squad and now shares that experience with local families in a safe, friendly school.</p>
    </div>
    <div class="awards">
      <h3 class="awards-title">AWARDS / ACHIEVEMENTS</h3>
      <p class="awards-sub">(Under Master Daniel's leadership)</p>
      <ul>
        <li>4 National Championship Titles</li>
        <li>10 State Medalists</li>
        <li>1 Regional Collegiate Conference Team Title</li>
        <li>Top Division Team Awards</li>
      </ul>
    </div>
  </section>

  <section class="panel info">
    <div class="info-card">
      <h2 class="section-title">TESTIMONIALS</h2>
      <p class="testimonial-name">LAURA <span class="accent">K.</span></p>
      <p class="testimonial">I started taking classes with Master Daniel a little over a year ago. He is patient, encouraging and makes every class fun. My son has grown so much in confidence and focus since joining.</p>
      <div class="offer">
        <span class="offer-tag">Special Offer</span>
        <p class="offer-amount">50% OFF</p>
        <p class="offer-detail">Trial Lessons &amp; Get a Free T-Shirt</p>
      </div>
      <div class="call">
        <svg width="20" height="20" viewBox="0 0 24 24" aria-hidden="true"><path fill="#fff" d="M6.6 10.8a15.1 15.1 0 0 0 6.6 6.6l2.2-2.2a1 1 0 0 1 1-.25 11.4 11.4 0 0 0 3.6.57 1 1 0 0 1 1 1V20a1 1 0 0 1-1 1A17 17 0 0 1 3 4a1 1 0 0 1 1-1h3.5a1 1 0 0 1 1 1c0 1.250.2 2.450.57 3.57a1 1 0 0 1-.25 1z"/></svg>
        <div>
          <p class="call-label">Call Us Today</p>
          <p class="call-number">(555) 010-2468</p>
        </div>
      </div>
      <div class="contact">
        <p><svg width="10" height="12" viewBox="0 0 10 14" aria-hidden="true"><path fill="#e3151b" d="M5 0a5 5 0 0 0-5 5c0 3.8 5 9 5 9s5-5.2 5-9a5 5 0 0 0-5-5zm0 7a2 2 0 1 1 0-4 2 2 0 0 1 0 4z"/></svg>Bright Path Dojo, 212 Maple Ridge Road</p>
        <p>Fairview, PA 10000</p>
        <p>www.brightpathdojo.example</p>
      </div>
      <div class="map" role="img" aria-label="Street map showing the school location"></div>
    </div>
  </section>

  <section class="panel cover">
    <div class="brand">
      <span class="brand-dot"></span>
      <span class="brand-name">Bright Path Dojo</span>
    </div>
    <div class="kids-photo" role="img" aria-label="Photo of two children in white uniforms doing a guard stance"></div>
    <div class="cover-rule"></div>
    <h1 class="headline">
      <span class="headline-top">Focus Your</span><br>
      <span class="headline-bottom">Child's Potential</span>
    </h1>
    <div class="web-bar">www.brightpathdojo.example</div>
    <div class="mascot" role="img" aria-label="Cartoon mascot in a uniform holding a training staff"></div>
  </section>

</main>
</body>
</html>
```